Healthcare technology firm needs business card layout. Logo provided.

We need a business card design for a new healthcare technology company called Kevrimo.com. The logo is already done so that will be used in the design. We assist patients and their families manage their personal health finances. Our initial product is our web site membership that includes educational content on your health benefits, tools, and downloadable forms.

We would like to see designs that use our existing logo or extend the logo in a creative way. Should be very consumer friendly.

```html
<!DOCTYPE html>
<html lang="en">
<head>
<meta charset="utf-8">
<title>Kevrimo.com business card</title>
<link rel="stylesheet" href="https://fonts.googleapis.com/css2?family=Montserrat:wght@500;600&family=Roboto+Condensed:wght@700&display=swap">
<style>
  :root {
    --page-bg: #e9e7e4;
    --card-white: #f4f4f4;
    --brand-blue: #2b9ad6;
    --brand-blue-light: #5cc1ee;
    --brand-blue-deep: #1b86c8;
    --logo-navy: #1d4f9a;
    --name-blue: #1f7fc4;
    --name-green: #7cc242;
    --text-grey: #5b5b5b;
  }
  * { margin: 0; padding: 0; box-sizing: border-box; }
  html, body {
    width: 963px;
    height: 1200px;
    overflow: hidden;
    background: var(--page-bg);
  }
  .sheet {
    position: relative;
    width: 963px;
    height: 1200px;
  }
  .card {
    position: absolute;
    left: 101px;
    width: 760px;
    height: 440px;
    border-radius: 26px;
    overflow: hidden;
    box-shadow: 0 10px 30px rgba(0,0,0,0.18);
  }
  .card-front {
    top: 110px;
    background: radial-gradient(ellipse at 35% 40%, var(--brand-blue-light) 0%, var(--brand-blue) 55%, var(--brand-blue-deep) 100%);
    display: flex;
    align-items: center;
    justify-content: center;
  }
  .wordmark {
    font-family: "Montserrat", sans-serif;
    font-weight: 600;
    color: var(--logo-navy);
    letter-spacing: 1px;
  }
  .card-front .wordmark { font-size: 72px; }

  .card-back {
    top: 650px;
    background: var(--card-white);
  }
  .back-band {
    position: absolute;
    left: 0; top: 0;
    width: 100%;
    height: 132px;
    background: var(--brand-blue);
    display: flex;
    align-items: center;
    justify-content: flex-end;
    padding-right: 48px;
  }
  .back-band .wordmark { font-size: 52px; }
  .band-rule {
    position: absolute;
    left: 0; top: 144px;
    width: 100%;
    height: 5px;
    background: var(--brand-blue);
  }
  .holder-name {
    position: absolute;
    left: 48px;
    top: 262px;
    font-family: "Roboto Condensed", sans-serif;
    font-weight: 700;
    font-size: 40px;
    line-height: 48px;
    letter-spacing: 0.5px;
  }
  .holder-name .first { color: var(--name-blue); }
  .holder-name .last { color: var(--name-green); }
  .contact {
    position: absolute;
    font-family: "Montserrat", sans-serif;
    font-weight: 500;
    font-size: 20px;
    line-height: 30px;
    color: var(--text-grey);
  }
  .contact-phones { left: 48px; top: 316px; }
  .contact-web { right: 48px; top: 250px; text-align: right; }
</style>
</head>
<body>
  <main class="sheet">
    <section class="card card-front" aria-label="Card front">
      <span class="wordmark">KEVRIMO</span>
    </section>

    <section class="card card-back" aria-label="Card back">
      <div class="back-band">
        <span class="wordmark">KEVRIMO</span>
      </div>
      <div class="band-rule"></div>

      <h1 class="holder-name"><span class="first">MARLA</span> <span class="last">QUINT</span></h1>

      <p class="contact contact-phones">tel: 0147 258 369<br>fax: 0147 258 360</p>
      <p class="contact contact-web">4 elm row. town<br>www.kevrimo.com<br>marla@kevrimo.com</p>
    </section>
  </main>
</body>
</html>
```